TMC Feedback sticker

We need a sticker design for our secondary school (aged 11 - 18). This is to allow teachers to provide feedback to students and vice-versa, having a conversation with the learner. I would love to have at least two different designs and it to be attractive, so that all can be included. I've attached the basic outline with the information to be presented. It should be A5 size, so that 2 of these can be fitted in.

Target Market(s)

Secondary school students

Industry/Entity Type

School

Font styles to use
Sans Serif

Requirements
Must have
• Attached details of the headings and enough space for all parties to respond.
Should not have
• Anything deemed inappropriate for secondary students

```html
<!DOCTYPE html>
<html lang="en">
<head>
<meta charset="UTF-8">
<title>Formative Feedback Sticker</title>
<link rel="stylesheet" href="https://fonts.googleapis.com/css2?family=Montserrat:wght@700&family=Arimo:wght@400&display=swap">
<style>
  :root {
    --page-bg: #ffffff;
    --card-light: #e2e2e2;
    --card-dark: #c4c4c4;
    --sheet: #f3f3f3;
    --sheet-edge: #d6d6d6;
    --orange: #f5a020;
    --orange-deep: #ee8a1e;
    --ink: #1e1e1e;
    --white: #ffffff;
  }
  html, body {
    margin: 0;
    width: 1200px;
    height: 821px;
    overflow: hidden;
    background: var(--page-bg);
  }
  .canvas {
    position: relative;
    width: 1200px;
    height: 821px;
  }
  .sticker {
    position: absolute;
    left: 328px;
    top: 30px;
    width: 494px;
    height: 692px;
    transform: scale(1.1);
    transform-origin: 0 0;
    background: linear-gradient(180deg, var(--card-light) 0%, var(--card-dark) 100%);
    overflow: hidden;
  }
  .sheet {
    position: absolute;
    left: 75px;
    top: 112px;
    width: 385px;
    height: 528px;
    background: var(--sheet);
    border: 1px solid var(--sheet-edge);
    box-sizing: border-box;
  }
  .sheet-title {
    position: absolute;
    left: 94px;
    top: 128px;
    margin: 0;
    font-family: "Montserrat", sans-serif;
    font-weight: 700;
    font-size: 11px;
    line-height: 14px;
    letter-spacing: 1.1px;
    color: var(--ink);
    white-space: nowrap;
  }
  .date-box {
    position: absolute;
    left: 350px;
    top: 58px;
    width: 118px;
    height: 30px;
    box-sizing: border-box;
    padding: 9px 0 0 14px;
    background: var(--orange);
    font-family: "Arimo", sans-serif;
    font-size: 10px;
    line-height: 12px;
    color: var(--ink);
    white-space: nowrap;
  }
  .label {
    position: absolute;
    left: 64px;
    box-sizing: border-box;
    padding: 8px 12px;
    background: linear-gradient(90deg, var(--orange), var(--orange-deep));
    font-family: "Arimo", sans-serif;
    font-size: 11px;
    line-height: 12px;
    color: var(--white);
    text-align: right;
    white-space: nowrap;
  }
  .label--strengths  { top: 152px; width: 122px; }
  .label--target     { top: 236px; width: 122px; }
  .label--action     { top: 330px; width: 74px; padding-top: 10px; padding-bottom: 10px; }
  .label--response   { top: 420px; width: 182px; }
  .label--reflection { top: 540px; width: 182px; }
</style>
</head>
<body>
<main class="canvas">
  <section class="sticker" aria-label="Formative feedback sticker">
    <div class="sheet"></div>

    <div class="date-box">Date: __________</div>

    <h1 class="sheet-title">FORMATIVE FEEDBACK Teacher C/L or H/L</h1>

    <div class="label label--strengths">Strengths<br>(What Went Well…)</div>
    <div class="label label--target">Target<br>(Even Better If…)</div>
    <div class="label label--action">Action</div>
    <div class="label label--response">Response<br>(from the student):</div>
    <div class="label label--reflection">Response and reflection<br>(from the teacher):</div>
  </section>
</main>
</body>
</html>
```